Empower our Electric Journey on the Web

We need a new website that can promote our services. Our three services that we offer are:
- Management of e-mobility charging stations
- Management of energy purchases
- Leasing of E-Mobility charging stations
- Energy billing of private electricity meters
The website should work responsively on PC, tablet and smartphone. In general, a simple navigation and an appealing design should be in the foreground. The website should give the customer the possibility to request , based pm a preset chexkbox chart and to get in contact with us.
Our logo works on black and white background.
Our slogan is:
Empower Your Electric Journey with Velmor Mobility
The 4 Pages should be the following:
Main Page, with info about us, why choose us,
2nd; services; what we sell and what are our services
3rd; Contact us, request an offer
4th, References about costumers and Work we already did, in the future we would like to integrate a Blog Post in this section in stead of references.

Target Market(s)

Landlords, Homeowners, Homeowner Associations

Industry/Entity Type

EV Chargers / E-Mobility

Coding

Coded - Design and coding required

Number of Pages Required

4 page

Requirements
Nice to have
• Pop up to our mailchimp newsletter subscription

```html
<!DOCTYPE html>
<html lang="en">
<head>
<meta charset="UTF-8">
<title>Velmor Mobility</title>
<link rel="stylesheet" href="https://fonts.googleapis.com/css2?family=Cinzel:wght@700&family=Poppins:wght@400;500;600&display=swap">
<style>
:root{
  --green:#3bb54a;
  --green-dark:#2f9e3c;
  --ink:#1b1b1b;
  --text:#3a3a3a;
  --muted:#555;
  --band:#f3f3f3;
  --black:#000;
  --white:#fff;
}
*{box-sizing:border-box;margin:0;padding:0}
html,body{width:1200px;height:3639px;overflow:hidden}
body{font-family:'Poppins',sans-serif;color:var(--text);background:var(--white);position:relative}
.abs{position:absolute}
.display{font-family:'Cinzel',serif;font-weight:700;color:var(--ink)}

/* brand */
.brand{display:flex;align-items:center;gap:12px;font-weight:600;color:var(--green);letter-spacing:2px;text-transform:uppercase;white-space:nowrap}
.brand-dot{width:30px;height:30px;background:var(--green);flex:none}

/* header */
.site-header{left:0;top:0;width:1200px;height:131px;background:var(--white)}
.site-header .brand{left:107px;top:44px;font-size:26px}
.main-nav{right:90px;top:60px;display:flex;gap:22px;font-size:14px;font-weight:600;color:var(--ink)}
.main-nav .active{color:var(--green);border-bottom:2px solid var(--green);padding-bottom:3px}

/* hero */
.hero{left:0;top:131px;width:1200px;height:689px;background:linear-gradient(110deg,#3a4150 0%,#5a6475 45%,#8b8f8a 70%,#6d6a5e 100%)}
.hero-eyebrow{left:92px;top:176px;color:var(--white);font-size:19px;font-weight:500}
.hero-title{left:91px;top:240px;width:600px;font-size:40px;line-height:50px;color:var(--white)}
.hero-title span{color:var(--green)}
.hero-cta{left:91px;top:447px;width:321px;height:66px;border:3px solid var(--white);color:var(--white);font-size:24px;display:flex;align-items:center;justify-content:center}

/* services */
.band{left:0;top:820px;width:1200px;height:1800px;background:var(--band)}
.section-title{left:0;width:1200px;text-align:center;font-size:40px}
.service-card{top:1072px;width:249px;height:379px;background:var(--white);text-align:center}
.service-img{position:absolute;left:15px;top:15px;width:219px;height:168px}
.service-card h3{position:absolute;left:8px;right:8px;top:202px;font-size:20px;font-weight:400;line-height:25px;color:var(--ink)}
.btn-outline,.btn-solid{position:absolute;left:44px;top:308px;width:154px;height:47px;display:flex;align-items:center;justify-content:center;font-size:17px}
.btn-outline{border:2px solid var(--green);color:var(--green)}
.btn-solid{background:var(--green);color:var(--white)}

/* about */
.about-photo{left:112px;top:1575px;width:400px;height:400px;border-radius:50%;border:7px solid var(--white);background:radial-gradient(circle at 60% 40%,#9aa3a6,#4d5558 70%)}
.about-inset{left:300px;top:1802px;width:192px;height:192px;border-radius:50%;border:7px solid var(--white);background:linear-gradient(135deg,#5fbfa8,#a7d8cb)}
.about-title{left:614px;top:1608px;font-size:40px}
.about-text{left:603px;top:1694px;width:438px;font-size:18.5px;line-height:24px;color:var(--muted)}
.about-btn{left:600px;top:1920px;width:153px;height:45px;background:var(--green);color:var(--white);font-size:20px;display:flex;align-items:center;justify-content:center}

/* why */
.why-item{top:2235px;width:260px;text-align:center}
.why-icon{width:97px;height:97px;margin:0 auto;border-radius:50%;border:3px solid var(--green);padding:5px}
.why-icon div{width:100%;height:100%;border-radius:50%;background:var(--green);display:flex;align-items:center;justify-content:center}
.why-item h4{margin-top:20px;font-size:17px;font-weight:600;color:var(--green)}
.why-item p{margin-top:22px;font-size:15px;line-height:21px;color:var(--ink)}

/* contact */
.contact{left:0;top:2620px;width:1200px;height:568px;background:var(--black)}
.contact-title{left:187px;top:45px;font-size:42px;color:var(--green)}
.field{border-bottom:3px solid var(--white);color:#d6d6d6;font-size:18px;padding-left:3px}
.contact-btn{left:193px;top:443px;width:343px;height:58px;background:var(--green);color:var(--white);font-size:20px;font-weight:500;display:flex;align-items:center;justify-content:center}
.contact .brand{left:750px;top:250px;font-size:30px}
.contact .brand-dot{width:40px;height:40px}

/* footer */
.footer .brand{left:63px;top:3366px;font-size:20px;letter-spacing:1px;gap:10px}
.footer .brand-dot{width:26px;height:26px}
.footer-col h5{font-size:21px;font-weight:500;color:var(--green);margin-bottom:20px}
.footer-col li{list-style:none;font-size:21px;line-height:34px;color:var(--ink);white-space:nowrap}
.footer-col li::before{content:"» ";color:var(--green)}
.news-title{left:860px;top:3290px;font-size:17px;font-weight:500;color:var(--green)}
.news-text{left:858px;top:3336px;width:290px;font-size:15px;line-height:25px;color:var(--ink)}
.news-form{left:860px;top:3404px;width:255px;height:53px;border:2px solid var(--green);padding:4px}
.news-form span{position:absolute;left:4px;top:14px;font-size:15px;color:#888}
.news-form b{position:absolute;right:4px;top:4px;width:100px;height:41px;background:var(--green);color:var(--white);font-size:15px;font-weight:500;display:flex;align-items:center;justify-content:center}
.divider{left:27px;top:3541px;width:1103px;height:2px;background:#ccc}
.copyright{left:99px;top:3570px;font-size:18px;color:var(--ink)}
.social{top:3573px;width:22px;height:22px;border-radius:50%}
</style>
</head>
<body>

<header class="site-header abs">
  <div class="brand abs"><span class="brand-dot"></span>Velmor Mobility</div>
  <nav class="main-nav abs">
    <span class="active">HOME</span><span>ABOUT US</span><span>SERVICES</span><span>WHY CHOOSE US</span><span>CONTACT US</span><span>BLOG</span>
  </nav>
</header>

<section class="hero abs" role="img" aria-label="Two engineers in hard hats inspecting solar panels under a cloudy sky">
  <p class="hero-eyebrow abs">VELMOR MOBILITY</p>
  <h1 class="hero-title display abs">Empower Your Electric Journey with <span>Velmor Mobility</span></h1>
  <div class="hero-cta abs">REQUEST AN OFFER</div>
</section>

<div class="band abs"></div>

<h2 class="section-title display abs" style="top:952px">Our Services</h2>

<article class="service-card abs" style="left:85px">
  <div class="service-img" role="img" aria-label="Car parked next to a charging station" style="background:linear-gradient(180deg,#c9ced3 0%,#8e9a8a 55%,#6d7470 100%)"></div>
  <h3>Management of E&#8209;mobility charging stations</h3>
  <div class="btn-outline">Read More</div>
</article>
<article class="service-card abs" style="left:342px">
  <div class="service-img" role="img" aria-label="Wind turbine over a green field" style="background:linear-gradient(180deg,#1f8f4a 0%,#5cbf6a 60%,#3e9e3a 100%)"></div>
  <h3>Management of energy purchases</h3>
  <div class="btn-solid">Read More</div>
</article>
<article class="service-card abs" style="left:601px">
  <div class="service-img" role="img" aria-label="Wall-mounted charging unit" style="background:linear-gradient(135deg,#e4e6e8 0%,#9aa0a6 50%,#3c4146 100%)"></div>
  <h3>Leasing of E&#8209;Mobility charging stations</h3>
  <div class="btn-outline">Read More</div>
</article>
<article class="service-card abs" style="left:857px">
  <div class="service-img" role="img" aria-label="Hand holding a charging connector" style="background:linear-gradient(135deg,#a2703f 0%,#6b4a2c 55%,#2a2420 100%)"></div>
  <h3>Energy billing of private electricity meters</h3>
  <div class="btn-outline">Read More</div>
</article>

<div class="about-photo abs" role="img" aria-label="Electric car plugged into a charger"></div>
<div class="about-inset abs" role="img" aria-label="EV charging sign"></div>
<h2 class="about-title display abs">About Us</h2>
<p class="about-text abs">Lorem ipsum dolor sit amet, consectetur adipiscing elit, sed do eiusmod tempor incididunt ut labore et dolore magna aliqua. Quis ipsum suspendisse ultrices gravida. Risus commodo viverra maecenas accumsan lacus vel facilisis. Quis ipsum suspendisse ultrices gravida. Risus facilisis. Risus viverra maecenas accumsan lacus vel facilisis.</p>
<div class="about-btn abs">Read More</div>

<h2 class="section-title display abs" style="top:2117px">Why Choose us</h2>

<div class="why-item abs" style="left:168px">
  <div class="why-icon"><div>
    <svg width="40" height="44" viewBox="0 0 40 44"><path d="M20 2 L37 8 V20 C37 32 29 39 20 42 C11 39 3 32 3 20 V8 Z" fill="#fff"/><path d="M20 13 l2.6 5.5 6 .7 -4.5 4 1.3 6 -5.4 -3 -5.4 3 1.3 -6 -4.5 -4 6 -.7z" fill="none" stroke="#3bb54a" stroke-width="1.6"/></svg>
  </div></div>
  <h4>24/7 CARE</h4>
  <p>Lorem ipsum dolor sit amet, consectetur adipiscing elit, maecenas accumsan lacus vel facilisis.</p>
</div>
<div class="why-item abs" style="left:475px">
  <div class="why-icon"><div>
    <svg width="48" height="48" viewBox="0 0 48 48" fill="#fff"><circle cx="18" cy="28" r="11"/><circle cx="32" cy="14" r="8"/><circle cx="18" cy="28" r="4" fill="#3bb54a"/><circle cx="32" cy="14" r="3" fill="#3bb54a"/></svg>
  </div></div>
  <h4>BEST SERVICE CHARGE</h4>
  <p>Lorem ipsum dolor sit amet, consectetur adipiscing elit, maecenas accumsan lacus vel facilisis.</p>
</div>
<div class="why-item abs" style="left:782px">
  <div class="why-icon"><div>
    <svg width="46" height="46" viewBox="0 0 46 46" fill="none" stroke="#fff" stroke-width="2.5"><ellipse cx="23" cy="23" rx="19" ry="8"/><ellipse cx="23" cy="23" rx="19" ry="8" transform="rotate(60 23 23)"/><ellipse cx="23" cy="23" rx="19" ry="8" transform="rotate(-60 23 23)"/><circle cx="23" cy="23" r="3" fill="#fff"/></svg>
  </div></div>
  <h4>DELIVERY ON TIME</h4>
  <p>Lorem ipsum dolor sit amet, consectetur adipiscing elit, maecenas accumsan lacus vel facilisis.</p>
</div>

<section class="contact abs">
  <h2 class="contact-title display abs">Contact us</h2>
  <div class="field abs" style="left:193px;top:140px;width:484px;height:42px">Enter &nbsp;Name</div>
  <div class="field abs" style="left:193px;top:208px;width:236px;height:42px">Enter Your E mail</div>
  <div class="field abs" style="left:454px;top:208px;width:218px;height:42px">Enter Phone number</div>
  <div class="field abs" style="left:193px;top:276px;width:484px;height:42px">&nbsp;Enter Your Address</div>
  <div class="field abs" style="left:193px;top:344px;width:484px;height:42px">&nbsp;&nbsp;Enter Mesage</div>
  <div class="contact-btn abs">REQEST AN OFFER</div>
  <div class="brand abs"><span class="brand-dot"></span>Velmor Mobility</div>
</section>

<footer class="footer">
  <div class="brand abs"><span class="brand-dot"></span>Velmor Mobility</div>
  <div class="footer-col abs" style="left:365px;top:3285px">
    <h5>Quick Links</h5>
    <ul><li>About</li><li>Services</li><li>Contact</li><li>Home</li></ul>
  </div>
  <div class="footer-col abs" style="left:580px;top:3285px">
    <h5>Information</h5>
    <ul><li>Terms &amp; Condition</li><li>Privacy Policy</li><li>About Us</li><li>Support</li></ul>
  </div>
  <p class="news-title abs">NEWSLETTER</p>
  <p class="news-text abs">Join our newsletter to stay up date with our latest updates</p>
  <div class="news-form abs"><span>Enter Your Email</span><b>Sign up</b></div>
  <div class="divider abs"></div>
  <p class="copyright abs">All rights reserved.Copyrights @ 2023</p>
  <span class="social abs" style="left:997px;background:#d6307a"></span>
  <span class="social abs" style="left:1034px;background:#1d9bf0"></span>
  <span class="social abs" style="left:1071px;background:#1877f2"></span>
</footer>

</body>
</html>
```